Australian Legal Practice would like a Web Design

I need a web design for a newly established law practice operating as Corvin Legal.

I would like the business to have an internet presence (via a website) essentially for the purpose of marketing and advertising. As the business grows (hopefully) I may be interested in providing general legal information as a means of establishing goodwill in the community and a easy and user friends contact method through the website.

The essence of the business is personal legal service based on local knowledge and therefore i want the website to present a picture of friendly professionalism, but mostly i want people who to be able to find the contact details of the business

I would like to have a map of the office location, and photos of the front of the office, the staff (me at the moment) and picture of law themed items and featuring the Corvin Legal logo.

The areas of law which Corvin Legal practises in are as follows:

commercial law
business sale and purchases
leases
conveyancing and property law
wills and estates
powers of attorney
general legal advice
succession planning

Reason: I have not had the opportunity to properly assess the designs and provide constructive feedback. I apologise for the inconvenience caused by my delay in providing feedback. Rob K.

Target Market(s)

Potential and existing clients of the firm
Other law firms
Associated stakeholders, i.e. Banks and real estate agents

Industry/Entity Type

Law Firm

Coding

Coded - Design and coding required

Number of Pages Required

2 page

Font styles to use
Sans Serif

Colors
85acd3
33a6d7
0456a4

Requirements
Must have
• Corvin Legal logo
• Map of the office location
• Picture of Rob Corvin (principal solicitor)
• Picture of the office
• Areas of Practice
• Address of office
• email address: rob.corvin@corvinlegal-example.com.au
• Physical address: 17 Ferncliff Road, Warrnock VIC 3391
• Phone number: (03) 5683 4917
• Facsimile number: (03) 5683 4038
• Space for a brief description of the firm and its competitive advantage
• Bar Guild Logo
• Links to the Bar Guild of Victoria
• Link to the practice standards Council
Nice to have
• coded to wordpress format

```html
<!DOCTYPE html>
<html lang="en">
<head>
<meta charset="utf-8">
<title>Corvin Legal</title>
<link href="https://fonts.googleapis.com/css2?family=Montserrat:wght@400;600;700;800&family=Roboto:wght@400;500&display=swap" rel="stylesheet">
<style>
:root{
  --blue:#0456a4;
  --sky:#33a6d7;
  --pale:#85acd3;
  --navy:#1f2a44;
  --ink:#222;
  --muted:#666;
  --grey:#f0f0f0;
  --dark:#2a2b2e;
  --orange:#d9891a;
  --white:#fff;
}
*{margin:0;padding:0;box-sizing:border-box}
html,body{width:1200px;height:2548px;overflow:hidden}
body{font-family:'Roboto',Arial,sans-serif;color:var(--ink);background:var(--white);position:relative}
.site-header{height:88px;display:flex;align-items:stretch;justify-content:space-between;padding:0 0 0 110px;background:var(--white)}
.brand{display:flex;align-items:center;gap:10px;font-family:'Montserrat',Arial,sans-serif;font-weight:700;font-size:30px;color:var(--blue);letter-spacing:1px}
.brand-mark{width:14px;height:14px;background:var(--blue)}
.main-nav{display:flex;margin-right:110px}
.main-nav a{display:flex;align-items:center;padding:0 22px;font-family:'Montserrat',Arial,sans-serif;font-size:13px;font-weight:600;color:var(--ink);text-decoration:none;letter-spacing:.5px}
.main-nav a.active{background:var(--blue);color:var(--white)}
.hero{position:relative;height:612px;background:linear-gradient(110deg,#3a2a1e 0%,#6b4a2c 35%,#2b2118 70%,#15110d 100%)}
.hero-art{position:absolute;inset:0}
.hero-copy{position:absolute;left:660px;top:250px;color:var(--white)}
.hero-copy h1{font-family:'Montserrat',Arial,sans-serif;font-weight:800;font-size:52px;line-height:58px;letter-spacing:1px}
.btn-orange{display:inline-block;margin-top:18px;background:var(--orange);color:var(--white);font-size:14px;padding:10px 22px;font-family:'Montserrat',Arial,sans-serif;font-weight:600}
.slide-arrow{position:absolute;top:280px;width:28px;height:52px;background:rgba(255,255,255,.25);display:flex;align-items:center;justify-content:center}
.slide-arrow.prev{left:0}.slide-arrow.next{right:0}
.principal{height:320px;background:var(--grey);display:flex;padding:0 110px;gap:60px}
.principal-text{width:470px;padding-top:62px}
.eyebrow{font-size:14px;color:var(--muted)}
.principal-text h2{font-family:'Montserrat',Arial,sans-serif;font-size:30px;font-weight:800;color:var(--navy);border-left:5px solid var(--blue);padding-left:12px;margin:8px 0 22px}
.principal-text h2 span{color:var(--blue)}
.principal-text p{font-size:13px;line-height:21px;color:var(--muted);margin-bottom:14px}
.principal-photo{width:450px;height:290px;margin-top:-10px;background:linear-gradient(#c9d3de,#a9b7c8)}
.practises-head{text-align:center;padding:66px 0 0;height:200px}
.practises-head h2{font-family:'Montserrat',Arial,sans-serif;font-size:32px;font-weight:800;color:var(--navy)}
.practises-head h2 span{color:var(--blue)}
.practises-head p{width:520px;margin:18px auto 0;font-size:13px;line-height:20px;color:var(--muted)}
.practise-grid{display:grid;grid-template-columns:repeat(4,300px);grid-auto-rows:220px}
.tile-photo{width:100%;height:100%}
.tile-text{padding:30px 28px;background:var(--white)}
.tile-text h3{font-family:'Montserrat',Arial,sans-serif;font-size:15px;font-weight:800;color:var(--navy);line-height:20px;margin-bottom:12px}
.tile-text p{font-size:13px;line-height:19px;color:var(--muted);width:200px}
.btn-blue{display:inline-block;margin-top:18px;background:var(--blue);color:var(--white);font-size:11px;padding:7px 14px}
.contact-head{height:120px;display:flex;align-items:center;justify-content:center;font-family:'Montserrat',Arial,sans-serif;font-size:34px;font-weight:400;color:var(--ink)}
.contact{position:relative;height:460px;background:var(--dark);color:var(--white);padding:98px 110px 0}
.contact-map{position:absolute;inset:0;background:linear-gradient(135deg,#2f3034,#24252a 60%,#2c2d31)}
.contact-info{position:relative}
.contact-info h2{font-family:'Montserrat',Arial,sans-serif;font-size:50px;font-weight:800;line-height:62px}
.contact-info address{font-style:normal;font-size:13px;line-height:28px;margin-top:34px;color:#ddd}
.social{display:flex;gap:12px;margin-top:20px}
.social span{width:26px;height:26px;border:2px solid #ccc;border-radius:50%}
.contact-form{position:absolute;left:760px;top:180px;width:320px}
.field{border-bottom:1px solid #888;height:38px;font-size:12px;color:#ccc;padding-top:14px}
.btn-outline{display:inline-block;margin-top:30px;border:1px solid #ccc;padding:8px 18px;font-size:12px}
.site-footer{height:88px;background:var(--blue);color:var(--white);font-size:13px;display:flex;align-items:center;justify-content:center}
</style>
</head>
<body>
<header class="site-header">
  <div class="brand"><span class="brand-mark"></span>CORVIN LEGAL</div>
  <nav class="main-nav">
    <a class="active">HOME</a><a>LAW PRACTISE</a><a>SERVICES</a><a>NEWS</a><a>BLOG</a><a>CONTACT US</a>
  </nav>
</header>

<section class="hero">
  <div class="hero-art" role="img" aria-label="Law themed still life: statue of justice, gavel, books and hourglass on a desk"></div>
  <div class="hero-copy">
    <h1>MAKING YOUR<br>PRIORITIES OURS</h1>
    <span class="btn-orange">Know More</span>
  </div>
  <div class="slide-arrow prev"><svg width="12" height="20"><path d="M10 2 2 10l8 8" fill="none" stroke="#fff" stroke-width="2"/></svg></div>
  <div class="slide-arrow next"><svg width="12" height="20"><path d="M2 2l8 8-8 8" fill="none" stroke="#fff" stroke-width="2"/></svg></div>
</section>

<section class="principal">
  <div class="principal-text">
    <div class="eyebrow">Welcome To Corvin Legal</div>
    <h2>PRINCIPAL <span>SOLICITOR</span></h2>
    <p>Lorem Ipsum is simply dummy text of the printing and typesetting industry. Lorem Ipsum has been the industry's standard dummy text ever since the 1500s, when an unknown printer took a galley of type and scrambled it to make a type specimen book.</p>
    <p>It has survived not only five centuries, but also the leap into electronic typesetting, remaining essentially unchanged.</p>
  </div>
  <div class="principal-photo" role="img" aria-label="Portrait of Rob Corvin, principal solicitor"></div>
</section>

<section class="practises-head">
  <h2>CORVIN LEGAL <span>PRACTISES</span></h2>
  <p>Lorem ipsum dolor sit amet, consectetur adipiscing elit, sed do eiusmod tempor incididunt ut labore et dolore magna aliqua.</p>
</section>

<section class="practise-grid">
  <div class="tile-photo" style="background:linear-gradient(135deg,#a9bfd6,#4d6a8a)" role="img" aria-label="Business people shaking hands at a meeting"></div>
  <div class="tile-text"><h3>COMMERCIAL LAW</h3><p>Lorem Ipsum is simply dummy text of the printing and typesetting industry.</p><span class="btn-blue">Read More</span></div>
  <div class="tile-photo" style="background:linear-gradient(135deg,#6fa3d6,#33a6d7)" role="img" aria-label="Laptop with business charts on a desk"></div>
  <div class="tile-text"><h3>BUSINESS SALE &amp;<br>PURCHASES LEASES</h3><p>Lorem Ipsum is simply dummy text of the printing and typesetting industry.</p><span class="btn-blue">Read More</span></div>

  <div class="tile-text"><h3>CONVEYANCING &amp;<br>PROPERTY LAW</h3><p>Lorem Ipsum is simply dummy text of the printing and typesetting industry.</p><span class="btn-blue">Read More</span></div>
  <div class="tile-photo" style="background:linear-gradient(135deg,#d8d8d8,#8a8a8a)" role="img" aria-label="Gavel beside a small model house"></div>
  <div class="tile-text"><h3>WILLS &amp; ESTATES</h3><p>Lorem Ipsum is simply dummy text of the printing and typesetting industry.</p><span class="btn-blue">Read More</span></div>
  <div class="tile-photo" style="background:linear-gradient(135deg,#e6e6e6,#7b6a55)" role="img" aria-label="Lawyer in a suit with scales of justice"></div>

  <div class="tile-photo" style="background:linear-gradient(135deg,#c9a27a,#4e3a2a)" role="img" aria-label="Client signing documents with a lawyer"></div>
  <div class="tile-text"><h3>GENERAL LEGAL ADVICE</h3><p>Lorem Ipsum is simply dummy text of the printing and typesetting industry.</p><span class="btn-blue">Read More</span></div>
  <div class="tile-photo" style="background:linear-gradient(135deg,#3a3a3a,#9a8560)" role="img" aria-label="Brass scales of justice and gavel"></div>
  <div class="tile-text"><h3>SUCCESSION PLANNING</h3><p>Lorem Ipsum is simply dummy text of the printing and typesetting industry.</p><span class="btn-blue">Read More</span></div>
</section>

<h2 class="contact-head">Contact Us</h2>

<section class="contact">
  <div class="contact-map" role="img" aria-label="Dark street map of the office location"></div>
  <div class="contact-info">
    <h2>GET IN TOUCH<br>WITH US.</h2>
    <address>
      17 Ferncliff Road, Warrnock VIC 3391<br>
      Phone: (03) 5683 4917 &nbsp; Fax: (03) 5683 4038<br>
      rob.corvin@corvinlegal-example.com.au
    </address>
    <div class="social"><span></span><span></span></div>
  </div>
  <form class="contact-form">
    <div class="field">Name</div>
    <div class="field">Email</div>
    <div class="field">Message</div>
    <span class="btn-outline">Submit Now</span>
  </form>
</section>

<footer class="site-footer">© 2017 Corvin Legal</footer>
</body>
</html>
```